Book cover needed for self help business book

Book cover needed and I will provide back cover blurb and barcode to the winning designer. Book may be too small for spine, but I will give you the page number details to confirm. Book information below:

Title: Nine Winters a Trader
Subtitle: Proven Market Methods That Keep Paying Off Now
Author: Maribel Okonte

Design should be clean, modern, and bold—something that appeals to everyday entrepreneurs and resellers. The cover should reflect grit, real-world hustle, and long-term wisdom without looking overly corporate or flashy. I am open to your creative ideas.

I am open to modern designs, but also designs of rugged old covers that simulate a book that may have aged over the years.

I prefer not to have pictures or silhouettes of people

Requirements
Nice to have
• I am open to modern designs, but also designs of rugged old covers that simulate a book that may have aged over the years.
Should not have
• Pictures or silhouettes of people

```html
<!DOCTYPE html>
<html lang="en">
<head>
<meta charset="utf-8">
<title>Nine Winters a Trader — Cover</title>
<link rel="stylesheet" href="https://fonts.googleapis.com/css2?family=Inter:wght@500;600;700;800&display=swap">
<style>
  :root {
    --cover-blue: #1889cc;
    --lake-blue: #1663bd;
    --lake-deep: #1350ad;
    --title-white: #f2f1ee;
    --accent-gold: #e99f0e;
    --author-white: #ffffff;
  }
  html, body {
    margin: 0;
    padding: 0;
    width: 982px;
    height: 1200px;
    overflow: hidden;
    background: var(--cover-blue);
  }
  .cover {
    position: relative;
    width: 982px;
    height: 1200px;
    overflow: hidden;
    background: var(--cover-blue);
    font-family: "Inter", sans-serif;
  }
  .lake-scene {
    position: absolute;
    left: 0;
    right: 0;
    top: 720px;
    bottom: 0;
    background: linear-gradient(
      to bottom,
      rgba(24, 137, 204, 0) 0%,
      rgba(22, 99, 189, 0.75) 14%,
      var(--lake-blue) 40%,
      var(--lake-deep) 100%
    );
  }
  .title-line {
    position: absolute;
    left: 0;
    right: 0;
    margin: 0;
    text-align: center;
    line-height: 1;
    font-weight: 700;
    text-transform: uppercase;
  }
  .title-nine {
    top: 150px;
    font-size: 330px;
    letter-spacing: -0.04em;
    color: var(--title-white);
  }
  .title-winters {
    top: 540px;
    font-size: 150px;
    letter-spacing: -0.02em;
    color: var(--accent-gold);
  }
  .title-trader {
    top: 726px;
    font-size: 100px;
    letter-spacing: -0.01em;
    color: var(--title-white);
  }
  .subtitle {
    position: absolute;
    left: 0;
    right: 0;
    top: 826px;
    margin: 0;
    text-align: center;
    font-size: 36px;
    font-weight: 600;
    line-height: 64px;
    color: var(--accent-gold);
  }
  .author {
    position: absolute;
    left: 0;
    right: 0;
    top: 1090px;
    margin: 0;
    text-align: center;
    font-size: 48px;
    font-weight: 600;
    line-height: 1;
    color: var(--author-white);
  }
</style>
</head>
<body>
  <main class="cover">
    <div class="lake-scene" role="img" aria-label="Blue-toned photo of a still lake with a small wooden rowboat, distant misty hills and a flock of birds flying low"></div>
    <h1 class="book-title">
      <span class="title-line title-nine">Nine</span>
      <span class="title-line title-winters">Winters</span>
      <span class="title-line title-trader">A Trader</span>
    </h1>
    <p class="subtitle">Proven Market Methods That Keep<br>Paying Off Now</p>
    <p class="author">Maribel Okonte</p>
  </main>
</body>
</html>
```